Flyer Design for Meridian Guild of Reflective Counsellors and Therapists (MGRCT)

We need a new flyer designed for MGRCT. We want to attract new members @ a tradeshow. Counsellors and Psychotherapists looking for a professional association with which to align themselves where they feel @ home because they share similar values.We would like to use the colours and leaves from our website which is www.mgrct-example.org if possible or similar colours and the photo of the tree in bloom from Facebook "stillwaterandtherapy". As well as our logo (www.mgrct-example.org), the TOVRA (www.tovra-example.org) logo as well somewhere in the bottom corner the Harmony Assembly logo (www.harmonyassembly-example.org).

Target Market(s)

Psychotherapists and Counsellors

Industry/Entity Type

Mental Health

Colors
876aae
b7a5cd
e4daeb
cadf82
abd036
9bcb3b

Requirements
Must have
• Logo
Nice to have
• Warm inviting photo of lotus flower
Should not have
• No monks

```html
<!DOCTYPE html>
<html lang="en">
<head>
<meta charset="utf-8">
<title>MGRCT Flyer</title>
<link href="https://fonts.googleapis.com/css2?family=Mulish:wght@400;600;700&display=swap" rel="stylesheet">
<style>
  :root {
    --purple-deep: #876aae;
    --purple-mid: #b7a5cd;
    --purple-pale: #e4daeb;
    --green-soft: #cadf82;
    --green: #abd036;
    --green-deep: #9bcb3b;
    --ink: #111111;
    --stage: #d4d4d4;
    --white: #ffffff;
  }
  * { margin: 0; padding: 0; box-sizing: border-box; }
  html, body { width: 873px; height: 1200px; overflow: hidden; }
  body {
    background: var(--stage);
    font-family: "Mulish", Arial, sans-serif;
    color: var(--ink);
    position: relative;
  }
  .page {
    position: absolute;
    left: 47px;
    width: 782px;
    background: var(--white);
    overflow: hidden;
  }
  .page-front { top: 37px; height: 553px; }
  .page-back { top: 606px; height: 555px; }

  .hero-photo {
    position: absolute; left: 0; top: 0; width: 782px; height: 310px;
    background:
      radial-gradient(ellipse 90px 150px at 50% 35%, rgba(255,255,240,0.95), rgba(255,255,255,0) 70%),
      radial-gradient(ellipse 110px 40px at 50% 78%, #eef0e6, rgba(230,230,230,0) 80%),
      linear-gradient(180deg, #b9b9b9 0%, #cfcfcf 60%, #d6d6d6 100%);
  }
  .logo-box {
    position: absolute; left: 22px; top: 20px; width: 140px; height: 128px;
    background: var(--white);
    display: flex; flex-direction: column; align-items: center; justify-content: center; gap: 12px;
    box-shadow: 0 1px 4px rgba(0,0,0,0.25);
  }
  .logo-name {
    font-family: "Mulish", Arial, sans-serif; font-weight: 400;
    font-size: 24px; letter-spacing: 1px; color: #333333;
  }
  .logo-dot { width: 40px; height: 40px; border-radius: 50%; background: #333333; }

  .tab {
    position: absolute;
    background: linear-gradient(180deg, var(--purple-pale), var(--purple-mid));
    border-radius: 4px;
    box-shadow: 0 2px 3px rgba(0,0,0,0.3);
    font-weight: 600; color: var(--ink);
    display: flex; align-items: center; justify-content: center; text-align: center;
    line-height: 1.05;
  }
  .tab-vision { left: 22px; top: 287px; width: 114px; height: 30px; font-size: 16px; }
  .tab-values { left: 22px; top: 413px; width: 137px; height: 36px; font-size: 14px; z-index: 2; }
  .tab-objective { left: 37px; top: 78px; width: 127px; height: 31px; font-size: 18px; z-index: 2; }
  .tab-goals { left: 37px; top: 255px; width: 127px; height: 31px; font-size: 18px; z-index: 2; }

  .vision-text {
    position: absolute; left: 22px; top: 327px; width: 762px;
    font-size: 8.6px; line-height: 14.5px; font-weight: 600;
  }

  .values-band {
    position: absolute; left: 0; top: 429px; width: 782px; height: 124px;
    background: linear-gradient(90deg, var(--purple-pale) 0%, #ece6ef 45%, #f6f6f0 62%, #e6eedb 100%);
  }
  .values-band .leaves {
    position: absolute; right: 0; top: 0; width: 300px; height: 124px;
    background: radial-gradient(ellipse 160px 90px at 70% 40%, rgba(155,203,59,0.35), rgba(202,223,130,0) 75%);
  }
  .bullets { list-style: none; position: absolute; }
  .bullets li { position: relative; padding-left: 14px; }
  .bullets li::before {
    content: ""; position: absolute; left: 0; top: 50%;
    width: 8px; height: 8px; margin-top: -4px; border-radius: 50%;
    border: 1px solid var(--purple-deep);
    background: radial-gradient(circle at 40% 40%, #ffffff, var(--purple-pale));
  }
  .values-list { left: 28px; top: 457px; width: 600px; font-size: 8.3px; font-weight: 600; line-height: 9px; z-index: 2; }
  .values-list li { margin-bottom: 6px; }
  .values-list li.two-line::before { top: 5px; }
  .web-corner {
    position: absolute; left: 606px; top: 515px; width: 176px; height: 38px; z-index: 2;
    background: var(--green);
    clip-path: polygon(36px 0, 100% 0, 100% 100%, 0 100%);
    display: flex; align-items: center; justify-content: flex-end; padding-right: 16px;
    font-size: 11.5px; font-weight: 700;
  }

  .back-top-band { position: absolute; left: 0; top: 57px; width: 782px; height: 11px; background: var(--green); }
  .lotus-photo {
    position: absolute; left: 0; top: 68px; width: 782px; height: 365px;
    background:
      radial-gradient(ellipse 220px 190px at 73% 68%, rgba(213,140,175,0.75), rgba(213,160,185,0) 75%),
      linear-gradient(180deg, #d9d2d8 0%, #e2d8d8 55%, #d9cfc6 100%);
  }
  .back-bottom-band { position: absolute; left: 0; top: 433px; width: 782px; height: 11px; background: var(--purple-deep); }
  .back-list { left: 37px; font-size: 10.2px; font-weight: 600; line-height: 15.6px; z-index: 2; }
  .objective-list { top: 122px; }
  .goals-list { top: 298px; }

  .footer-logo {
    position: absolute; left: 33px; top: 455px; width: 80px;
    display: flex; flex-direction: column; align-items: center; gap: 8px;
  }
  .footer-logo .logo-name { font-size: 19px; }
  .footer-logo .logo-dot { width: 36px; height: 36px; }
  .contact { position: absolute; top: 457px; font-size: 10.5px; line-height: 10.5px; font-weight: 600; }
  .contact-main { left: 187px; }
  .contact-branch { left: 494px; }
  .contact h3 { color: var(--purple-deep); font-size: 11.5px; line-height: 10.5px; font-weight: 700; margin-bottom: 10px; }
</style>
</head>
<body>

<section class="page page-front">
  <div class="hero-photo" role="img" aria-label="Glowing white lotus flower with sparkles rising, reflected on still water"></div>
  <div class="logo-box">
    <span class="logo-name">MGRCT</span>
    <span class="logo-dot"></span>
  </div>

  <div class="tab tab-vision">Our Vision</div>
  <p class="vision-text">The purpose of The Meridian Guild of Reflective Counsellors and Therapists (MGRCT), a TOVRA Member Association, is to bring the whole philosophy and practice of Buddhism (the dhamma), totherapists and counsellors, using innovative educational experiences. The benefits of introducing Buddhist practices into mental health is now scientifically validated, as increasing the effectiveness of Western psychotherapeutic approaches, as well as taking care of therapists in particular ‘burnout.’ There is much to benefit us, as well as those we work with, in our desire to integrate Psychotherapy with Buddhism. So, MGRCT has developed and has been runninga two-year professional training course in Buddhism and Psychotherapy, since 2008.The next training will begin July 2016.</p>

  <div class="values-band">
    <div class="leaves" role="img" aria-label="Soft green leaves drifting across the corner"></div>
  </div>
  <div class="tab tab-values">Some of Our<br>Values</div>
  <ul class="bullets values-list">
    <li>We care about therapists</li>
    <li>We strive to be of service to our members and all those we come into contact with humility, fairness, patience and compassion</li>
    <li class="two-line">We value the ongoing need for education for therapists but we also value the balance between the mind, the body and the spirit, knowing that all those need to be nourished</li>
    <li class="two-line">We work in warm, generous, spirited partnership with others and we are open to working within and across sectors to influence and co-develop initiatives.</li>
  </ul>
  <div class="web-corner">www.mgrct-example.org</div>
</section>

<section class="page page-back">
  <div class="back-top-band"></div>
  <div class="lotus-photo" role="img" aria-label="Close-up of a pink lotus bud on a soft blurred background"></div>
  <div class="back-bottom-band"></div>

  <div class="tab tab-objective">Objective</div>
  <ul class="bullets back-list objective-list">
    <li>To provide a philosophical base,standardsand ethics for the practice of Buddhist Counselling and Psychotherapy.</li>
    <li>Maintain unique professional development of its members, as well as provide a warm and supportive community of therapists.</li>
    <li>Develop a professional organisational structure that supports the practice of Buddhist Counselling and Psychotherapy;</li>
    <li>Provide an innovative education, training and research in Buddhist Counselling and Psychotherapy;</li>
    <li>Promote Buddhist Counselling and Psychotherapy in the community;</li>
    <li>Provide accreditation practices that will support the highest quality practice in Buddhist Counselling and Psychotherapy; and</li>
    <li>Work collaboratively and beneficially with other Buddhist and Counselling and Psychotherapy Organisations.</li>
  </ul>

  <div class="tab tab-goals">Our Goals</div>
  <ul class="bullets back-list goals-list">
    <li>To present Buddhism in a through way</li>
    <li>To explore and discuss dhamma and how it can improve the effectiveness of a therapist’s life</li>
    <li>To provide ongoing education in all aspects of Buddhism for mental health professionals</li>
    <li>To develop a dynamic organisation that stays attuned to changes in Buddhism as it is expressed in the West</li>
    <li>To develop a strong membership/community</li>
    <li>To develop a relevant and important voice in the community</li>
    <li>To develop a unique professional identity</li>
    <li>To encourage positive social change</li>
  </ul>

  <div class="footer-logo">
    <span class="logo-name">MGRCT</span>
    <span class="logo-dot"></span>
  </div>
  <address class="contact contact-main" style="font-style:normal">
    <h3>Meridian Guild of Reflective<br>Counsellors and Therapists</h3>
    PO Box 4820<br>Larkfield Junction 2190 NSW<br>Australia<br>Email: info@stillwaterandtherapy.org
  </address>
  <address class="contact contact-branch" style="font-style:normal">
    <h3>Meridian Guild of Reflective<br>Counsellors and Therapists</h3>
    Queensland Branch<br>Email: qld@stillwaterandtherapy.org
  </address>
</section>

</body>
</html>
```